Anzeigengestaltung für eine Stellenanzeige
Zielgruppe
Stellenanzeige
Wir sind eine Druckerei. Wir suchen für unsere Druckerei einen Buchhalter/in oder bzw. auch für das Rechnungswesen.
Aufgabenstellung
Wir möchten eine Stellenanzeige mit klarer und schneller Wirkung , keine Fließtextanzeige und einer unnötigen Beschreibung wie toll unserer Druckerei ausgestattet ist. Die Anzeige darf bunt und lustig sein Wortspiele wie Zahlenbändiger o.ä. sind erlaubt. Die Stelle soll für 30 bis 40 Stunden Wochenarbeitsstunden ausgeschrieben sein.
Mehr möchten wir gar nicht sagen wir sind ja nicht die kreativsten :-)
Unsere Hausfarbe sind HKS 38 und HKS 6

```html
<!DOCTYPE html>
<html lang="de">
<head>
<meta charset="utf-8">
<title>Stellenanzeige Buchhalter*in – Kessler &amp; Rund</title>
<link rel="stylesheet" href="https://fonts.googleapis.com/css2?family=Barlow+Condensed:wght@500;600;700&family=Kaushan+Script&display=swap">
<style>
  :root {
    --orange: #f08a0c;
    --orange-light: #f6aa4e;
    --orange-deep: #e07c05;
    --navy: #0c2849;
    --white: #ffffff;
  }
  * { margin: 0; padding: 0; box-sizing: border-box; }
  html, body { width: 1200px; height: 800px; overflow: hidden; background: var(--white); }
  .ad {
    position: relative;
    width: 1200px;
    height: 800px;
    font-family: "Barlow Condensed", "Arial Narrow", sans-serif;
    text-transform: uppercase;
  }
  .ad__stage {
    position: absolute; left: 0; top: 0;
    width: 1200px; height: 764px;
    background: radial-gradient(ellipse at 78% 18%, var(--orange-light) 0%, var(--orange) 55%, var(--orange-deep) 100%);
    overflow: hidden;
  }
  .ad__photo {
    position: absolute; left: 45px; top: 105px;
    width: 430px; height: 340px;
    border-radius: 48% 52% 46% 54% / 55% 50% 50% 45%;
    background: radial-gradient(ellipse at 50% 50%, #4a4d52 0%, #6b6358 45%, rgba(224,124,5,0.4) 80%, rgba(224,124,5,0) 100%);
  }
  .ad__bubble {
    position: absolute; left: 480px; top: 50px;
    width: 680px; height: 420px;
  }
  .ad__headline {
    position: absolute; left: 570px; top: 120px;
    width: 580px;
    font-family: "Kaushan Script", cursive;
    text-transform: none;
    font-weight: 400;
    color: var(--navy);
    line-height: 0.95;
    transform: rotate(-6deg);
  }
  .ad__headline-line { display: block; font-size: 112px; }
  .ad__headline-line--second { padding-left: 130px; font-size: 130px; }
  .job {
    position: absolute; left: 42px; top: 522px;
    color: var(--white);
  }
  .job__title {
    display: inline-block;
    background: var(--navy);
    padding: 6px 10px 4px;
    font-size: 38px; font-weight: 600;
    line-height: 50px;
    margin-bottom: 8px;
  }
  .job__facts { list-style: none; font-size: 33px; font-weight: 500; line-height: 39px; }
  .pitch {
    position: absolute; left: 523px; top: 515px;
    width: 650px;
    color: var(--white);
    font-size: 32px; font-weight: 500; line-height: 39px;
  }
  .pitch__call { margin-top: 16px; }
  .ad__footer {
    position: absolute; left: 0; top: 764px;
    width: 1200px; height: 36px;
  }
  .ad__footer {
    top: 719px; height: 81px;
    background: var(--white);
    display: flex; align-items: center; justify-content: space-between;
    padding: 0 42px 0 42px;
  }
  .ad__stage { height: 719px; }
  .brand { color: var(--navy); }
  .brand__name { font-size: 38px; font-weight: 700; line-height: 1; }
  .brand__claim { font-size: 14px; font-weight: 600; letter-spacing: 1px; text-align: right; }
  .apply { color: var(--navy); font-size: 31px; font-weight: 600; }
</style>
</head>
<body>
<div class="ad">
  <div class="ad__stage">
    <div class="ad__photo" role="img" aria-label="Foto: Fernglas, durch ein gerissenes Loch im orangefarbenen Papier schauend"></div>

    <svg class="ad__bubble" viewBox="0 0 680 420" aria-hidden="true">
      <path d="M330 55 C470 45 640 80 668 210 C690 320 560 390 400 388 C330 387 300 385 250 390 L180 412 L210 375 C120 350 85 290 90 220 C95 110 200 62 330 55 Z" fill="var(--white)"/>
      <g stroke="var(--white)" stroke-width="5" stroke-linecap="round" fill="none">
        <line x1="630" y1="62" x2="625" y2="88"/>
        <line x1="668" y1="80" x2="648" y2="100"/>
        <line x1="680" y1="120" x2="655" y2="128"/>
        <path d="M110 330 Q118 358 145 372"/>
        <path d="M95 345 Q105 372 130 385"/>
      </g>
    </svg>

    <h1 class="ad__headline">
      <span class="ad__headline-line">Wir suchen</span>
      <span class="ad__headline-line ad__headline-line--second">Dich!</span>
    </h1>

    <section class="job">
      <h2 class="job__title">Buchhalter*in gesucht</h2>
      <ul class="job__facts">
        <li>30 bis 40 Stunden / Woche</li>
        <li>Kaufmännischer Abschluss</li>
        <li>Teamfähig</li>
      </ul>
    </section>

    <section class="pitch">
      <p>Furchtlose Zahlenbändiger*innen, die bei Begriffen<br>wie „Soll und Haben“ einen kühlen Kopf bewahren und<br>sich täglich 6–8 Stunden gegen die EDV tapfer<br>zu wehren wissen!</p>
      <p class="pitch__call">Das trifft auf dich zu? Dann bewirb dich noch heute!</p>
    </section>
  </div>

  <footer class="ad__footer">
    <div class="brand">
      <div class="brand__name">Kessler &amp; Rund</div>
      <div class="brand__claim">Druck mit Herz</div>
    </div>
    <p class="apply">Schick deine Bewerbung an: k.kessler@kesslerundrund.de</p>
  </footer>
</div>
</body>
</html>
```